Re-design Consulting Web Site (B2B Sales Consultancy for Early Stage SaaS/tech firms)

I have just built a web site in WordPress.

Here is the link:- https://tawny-walrus-518306.sitehaven.example/

(ALL PAGES AND SITE CONTENT IS FOUND ON THE LINK)

It's not a bad site. It's just a bit messy in terms of consistency and styling - font usage, spacing between sections etc. I want it to be slick, stylish and professional.

My audience is CEOs/Founders of B2B Tech / SaaS firms.

One of the issues is font choice and inconsistent font sizing maybe.

The site is currently in WordPress but I don't mind it being built outside of WordPress provided it will be easy to manage and update.

Some designs I kind of like (although do not just copy these - I want original designs).
https://layouts.brisklane.example/ko/office4/
https://fernpath.lumidock.example/ledger-advisory/

OTHER NOTES:

I don't to use too many photos on the new design. We can keep the photos where I am shown.

I would like to use more custom graphics and abstract graphics.

NOTE: One designer started a design in Draftloom but she had a family emergency and had to cancel the project. She what she did. It's ok - https://www.draftloom.example/design/q7Tzw2PLmkXvB4hNcYsAeG/Untitled?node-id=0-1

Target Market(s)

CEOs / Founders of B2B SaaS firms in the UK and US

Industry/Entity Type

SaaS, Tech, Consulting, Coaching, IT, Management Consulting.

Number of Pages Required

5+ page

Font styles to use
Serif
Sans Serif
Other font styles liked:
• Poppins or something similar/better.

Colors

Designer to choose colors to be used in the design.

Requirements
Must have
• Impactful headlines. Reorganise the information presented on my current side much better. Spacings and alignments must be spot on. Use Poppins as the font (or something similar). Abstract/custom graphics. A nice colour palette with 3-4 colors. the 'Engagement Plans' section on the homepage needs to be redesigned completely so the information is presented almost in accordian style or someting.
Nice to have
• Try graph paper style as the header background. See this Draftloom design one designer started - https://www.draftloom.example/design/q7Tzw2PLmkXvB4hNcYsAeG/Untitled?node-id=0-1
Should not have
• Do not use Merriweather, Roboto or Aria fonts. No not use red. Please do NOT simply present the existing UI, design and Information Architecture in the same or similar form as the current site. This defeats the purpose. I want to see NEW designs and a better way of organising and presenting the existing site content.

```html
<!DOCTYPE html>
<html lang="en">
<head>
<meta charset="utf-8">
<title>Harlow Vance Sales Advisory – Homepage Concepts</title>
<link rel="stylesheet" href="https://fonts.googleapis.com/css2?family=Poppins:wght@400;500;600;700;800&display=swap">
<style>
:root{
  --board:#ecebfb;
  --blue:#1d1ddb;
  --blue-deep:#1414b8;
  --navy:#0d0d4a;
  --ink:#16163a;
  --muted:#6b6b85;
  --line:#dedded;
  --soft:#f3f3f7;
  --white:#ffffff;
  --yellow:#f4e23c;
  --tick:#2fb36b;
}
*{box-sizing:border-box;margin:0;padding:0}
html,body{width:1200px;height:3960px;overflow:hidden}
body{background:var(--board);font-family:"Poppins",Arial,sans-serif;color:var(--ink);position:relative}
.page{position:absolute;top:40px;width:552px;height:3870px;background:var(--white);overflow:hidden;display:flex;flex-direction:column;box-shadow:0 6px 24px rgba(20,20,80,.08)}
.page--a{left:32px}
.page--b{left:616px}
p{font-size:8px;line-height:1.55;color:var(--muted)}
.eyebrow{font-size:7px;font-weight:600;letter-spacing:.14em;color:var(--blue);text-transform:uppercase;text-align:center}
.section-title{font-size:22px;font-weight:800;text-align:center;letter-spacing:-.01em;color:var(--ink)}
.btn{display:inline-block;background:var(--blue);color:var(--white);font-size:7px;font-weight:600;padding:7px 14px;border-radius:3px}
.btn--light{background:var(--white);color:var(--blue)}
.btn--outline{background:transparent;border:1px solid var(--ink);color:var(--ink)}

/* hero */
.hero{height:290px;position:relative;color:var(--white);padding:0 28px;display:flex;flex-direction:column}
.page--a .hero{background:linear-gradient(160deg,#2a2a3a 0%,#55566a 45%,#1c1c2b 100%)}
.page--b .hero{background:var(--blue)}
.hero-photo{position:absolute;inset:0;background:linear-gradient(115deg,rgba(15,15,30,.85) 0%,rgba(40,42,60,.55) 55%,rgba(110,112,130,.5) 100%)}
.hero-art{position:absolute;right:22px;top:52px;width:190px;height:170px;border-radius:50% 50% 46% 54%;background:radial-gradient(circle at 45% 45%,#fff36a 0%,var(--yellow) 60%,#e0cd22 100%)}
.nav{position:relative;height:34px;display:flex;align-items:center;justify-content:space-between}
.brand{display:flex;align-items:center;gap:5px;font-size:6.5px;font-weight:700;letter-spacing:.06em;line-height:1.2;text-transform:uppercase}
.brand-mark{width:12px;height:12px;background:var(--white)}
.nav-links{display:flex;gap:11px;font-size:6px;font-weight:500;opacity:.9}
.nav-icons{display:flex;gap:5px}
.nav-icons span{width:8px;height:8px;border-radius:50%;background:rgba(255,255,255,.85)}
.hero-body{position:relative;margin-top:26px;width:100%}
.page--a .hero-body{text-align:center}
.page--b .hero-body{width:300px}
.hero-title{font-size:27px;font-weight:800;line-height:1.08;letter-spacing:-.01em}
.page--a .hero-title{color:#4a5cff}
.page--a .hero-title em{font-style:normal;color:var(--white)}
.page--b .hero-title em{font-style:normal}
.hero-sub{font-size:8px;color:rgba(255,255,255,.85);margin:10px 0 12px;line-height:1.5}
.hero .btn{background:var(--white);color:var(--blue)}
.page--a .hero .btn{background:var(--blue);color:var(--white)}
.logo-row{position:relative;margin-top:auto;margin-bottom:22px;display:flex;justify-content:space-between;align-items:center;border-top:1px solid rgba(255,255,255,.2);padding-top:14px}
.logo-row span{font-size:10px;font-weight:700;letter-spacing:.02em;color:var(--white)}

/* spotlight */
.spotlight{height:420px;padding:22px 28px 0}
.spotlight .section-title{margin:3px 0 18px}
.spot-row{display:flex;gap:16px;margin-bottom:14px}
.spot-img{width:250px;height:170px;flex:none;border-radius:2px}
.spot-img--city{background:linear-gradient(170deg,#cfd2db 0%,#7b7f8e 50%,#3c3f4c 100%)}
.spot-img--person{position:relative;background:linear-gradient(150deg,#c9c3b8 0%,#8b8478 60%,#5c564e 100%)}
.badge{position:absolute;left:-18px;bottom:-8px;width:70px;height:52px;background:var(--blue);color:var(--white);display:flex;align-items:center;gap:5px;padding:0 8px}
.badge b{font-size:20px;font-weight:800}
.badge small{font-size:5.5px;line-height:1.3}
.spot-text h4{font-size:7px;font-weight:700;letter-spacing:.1em;color:var(--ink);margin:0 0 3px}
.spot-text p{margin-bottom:7px;font-size:7px}

/* stats */
.stats{height:100px;background:var(--blue);display:flex}
.stat{flex:1;display:flex;flex-direction:column;justify-content:center;padding:0 20px;color:var(--white);border-right:1px solid rgba(255,255,255,.18)}
.stat:last-child{border-right:0}
.stat b{font-size:19px;font-weight:800;line-height:1.05}
.stat small{font-size:6.5px;opacity:.8;margin-top:5px}

/* fail */
.fail{height:130px;padding:20px 28px;display:flex;gap:18px}
.fail-list{width:250px;display:flex;flex-direction:column;gap:6px}
.fail-list div{border:1px solid var(--line);font-size:7px;font-weight:500;padding:8px 10px;display:flex;justify-content:space-between}
.fail-list div:first-child{border-color:var(--blue);color:var(--blue)}
.fail-copy h3{font-size:15px;font-weight:800;margin-bottom:6px}

/* ideal */
.ideal{height:230px;padding:24px 28px 0;border-top:1px solid var(--line)}
.ideal .section-title{margin:3px 0 20px}
.ideal-cols{display:flex;gap:22px}
.ideal-col{flex:1;text-align:center}
.ideal-col h4{font-size:8px;font-weight:700;letter-spacing:.06em;margin-bottom:6px}
.ideal-col p{margin-bottom:12px}

/* results */
.results{height:330px;background:var(--soft);padding:40px 28px 0}
.results .section-title{margin:3px 0 22px}
.video-row{display:flex;gap:6px}
.video{flex:1;height:120px;position:relative}
.video:nth-child(1){background:linear-gradient(160deg,#bfb7a9,#6f675c)}
.video:nth-child(2){background:linear-gradient(160deg,#aab0bd,#555b68)}
.video:nth-child(3){background:linear-gradient(160deg,#c8beb0,#7a7064)}
.video:nth-child(4){background:linear-gradient(160deg,#9fa7b5,#4d5463)}
.play{position:absolute;left:50%;top:50%;width:20px;height:20px;margin:-10px 0 0 -10px;border-radius:50%;background:rgba(255,255,255,.92)}
.play svg{position:absolute;left:7px;top:5px}

/* testimonials */
.testimonials{height:330px;padding:28px 28px 0;display:flex;gap:18px}
.quote{flex:1;text-align:center}
.quote-mark{width:26px;height:26px;margin:0 auto 10px;background:var(--navy);display:flex;align-items:center;justify-content:center}
.quote-card{border:1px solid var(--line);padding:14px 12px;position:relative}
.quote-card p{font-size:7px}
.quote-card::after{content:"";position:absolute;left:50%;bottom:-7px;width:12px;height:12px;margin-left:-6px;background:var(--white);border-right:1px solid var(--line);border-bottom:1px solid var(--line);transform:rotate(45deg)}
.avatar{width:32px;height:32px;border-radius:50%;background:linear-gradient(150deg,#c7c0b5,#7e766a);margin:18px auto 6px}
.quote-name{font-size:7.5px;font-weight:700}
.quote-role{font-size:6.5px;color:var(--muted)}

/* recent */
.recent{height:520px;padding:26px 28px 0;border-top:1px solid var(--line)}
.recent .section-title{margin:3px 0 18px}
.recent-body{display:flex;gap:18px}
.recent-tabs{width:200px;flex:none;display:flex;flex-direction:column;gap:6px}
.recent-tabs div{font-size:7px;font-weight:500;padding:9px 10px;border:1px solid var(--line)}
.recent-tabs div.is-active{border-color:var(--blue);color:var(--blue);font-weight:600}
.recent-copy h4{font-size:7px;font-weight:700;letter-spacing:.1em;margin-bottom:3px}
.recent-copy p{font-size:7px;margin-bottom:9px}

/* plans */
.plans{height:640px;padding:26px 28px 0}
.plans .section-title{margin:3px 0 16px}
.plan{border:1px solid var(--line);margin-bottom:6px}
.plan.is-open{border:1.5px solid var(--blue)}
.plan-head{display:flex;align-items:center;justify-content:space-between;padding:10px 12px;font-size:8px;font-weight:700}
.plan-head small{font-weight:400;color:var(--muted);font-size:6.5px;margin-left:8px}
.plan-body{padding:0 12px 12px}
.plan-group{border-top:1px solid var(--line);padding:8px 0}
.plan-group h5{font-size:6.5px;font-weight:700;letter-spacing:.08em;color:var(--blue);margin-bottom:4px}
.plan-item{display:flex;justify-content:space-between;align-items:center;font-size:6.5px;color:var(--muted);padding:3px 0}
.tick{width:9px;height:9px;border-radius:50%;background:var(--tick);display:flex;align-items:center;justify-content:center;flex:none}

/* steps */
.steps{height:420px;padding:26px 28px 0;border-top:1px solid var(--line)}
.steps .section-title{margin:3px 0 6px}
.steps-intro{text-align:center;margin:0 30px 18px}
.step-grid{display:grid;grid-template-columns:1fr 40px 1fr;row-gap:16px;align-items:center}
.step{border:1px solid var(--line);padding:14px 12px;text-align:center;height:118px}
.step.is-first{border:1.5px solid var(--blue)}
.step-num{width:26px;height:26px;margin:0 auto 8px;display:flex;align-items:center;justify-content:center;font-size:11px;font-weight:700;background:var(--soft);color:var(--ink)}
.step.is-first .step-num{background:var(--blue);color:var(--white)}
.step h4{font-size:7px;font-weight:700;letter-spacing:.06em;margin-bottom:4px}
.step p{font-size:6.5px}
.arrow{display:flex;justify-content:center}

/* cta */
.ready{height:220px;background:var(--blue);color:var(--white);text-align:center;padding:46px 60px 0}
.ready h2{font-size:22px;font-weight:800;margin-bottom:10px}
.ready p{color:rgba(255,255,255,.85);margin-bottom:16px}
.unlock{height:200px;background:var(--navy);color:var(--white);display:flex;align-items:center;padding:0 28px;gap:20px}
.unlock-copy{flex:1}
.unlock .eyebrow{text-align:left;color:#8f8fff;margin-bottom:4px}
.unlock h2{font-size:20px;font-weight:800;line-height:1.1;margin-bottom:12px}
.signup{display:flex}
.signup span{flex:1;background:var(--white);color:var(--muted);font-size:6.5px;padding:7px 8px}
.signup b{background:var(--blue);font-size:6.5px;font-weight:600;padding:7px 10px}
.unlock-photo{width:200px;height:140px;background:linear-gradient(150deg,#cfc8bd,#7d766b);position:relative}
.footer{height:40px;background:var(--navy);border-top:1px solid rgba(255,255,255,.12);display:flex;align-items:center;justify-content:center;font-size:6.5px;color:rgba(255,255,255,.7)}
</style>
</head>
<body>

<!-- Concept A -->
<main class="page page--a">
  <header class="hero">
    <div class="hero-photo" role="img" aria-label="Dark city office towers photographed from street level"></div>
    <nav class="nav">
      <div class="brand"><span class="brand-mark"></span><span>Harlow Vance<br>Sales Advisory</span></div>
      <div class="nav-links"><span>Home</span><span>About</span><span>Services</span><span>Results</span><span>Insights</span><span>Contact</span></div>
      <div class="nav-icons"><span></span><span></span><span></span></div>
    </nav>
    <div class="hero-body">
      <h1 class="hero-title">Fractional GTM<br><em>Leadership for SaaS Firms</em></h1>
      <p class="hero-sub">Unlock your SaaS Hyper-growth Potential.<br>Propelling from Launch to $1M ARR, Scaling Seamlessly to $10M ARR.</p>
      <span class="btn">Book a 30-min Discovery Call Today</span>
    </div>
    <div class="logo-row"><span>Vectrona</span><span>Norvale</span><span>Marrowby</span><span>Quillon</span><span>Tallisk</span></div>
  </header>

  <section class="spotlight">
    <div class="eyebrow">Case Study</div>
    <h2 class="section-title">PROJECT SPOTLIGHT</h2>
    <div class="spot-row">
      <div class="spot-img spot-img--city" role="img" aria-label="Looking up at glass office towers"></div>
      <div class="spot-text">
        <h4>SITUATION</h4>
        <p>A seed-funded SaaS platform had strong product interest but no repeatable sales motion, founder-led deals and a stalled pipeline heading into its next round.</p>
        <h4>ACTION</h4>
        <p>We rebuilt the go-to-market plan, defined the ideal customer profile, set up outbound playbooks and coached the first two account executives through live deals.</p>
        <p>Weekly pipeline reviews and clear stage criteria gave the founders confidence in the forecast within one quarter.</p>
      </div>
    </div>
    <div class="spot-row">
      <div class="spot-text">
        <h4>RESULT</h4>
        <p>Qualified pipeline tripled in six months and the team closed its largest enterprise contract to date, setting up a strong Series A story for investors.</p>
        <p>The sales function now runs without founder involvement in every deal, freeing leadership to focus on product and hiring.</p>
      </div>
      <div class="spot-img spot-img--person" role="img" aria-label="Portrait of the consultant at his desk">
        <div class="badge"><b>24</b><small>Years in<br>B2B sales</small></div>
      </div>
    </div>
  </section>

  <section class="stats">
    <div class="stat"><b>$135M<br>OVERALL</b><small>Revenue generated for clients</small></div>
    <div class="stat"><b>$135M<br>OVERALL</b><small>Pipeline created across markets</small></div>
    <div class="stat"><b>$135M<br>OVERALL</b><small>Funding raised by clients</small></div>
  </section>

  <section class="fail">
    <div class="fail-list">
      <div>95% of SaaS firms fail <span>+</span></div>
      <div>We help SaaS to spot where sales fits in <span>+</span></div>
      <div>Leveraging our GTM strategy for SaaS to scale <span>+</span></div>
    </div>
    <div class="fail-copy">
      <h3>95% of SaaS firms fail.</h3>
      <p>Most early-stage SaaS companies never find a repeatable way to sell. Without a clear go-to-market plan, growth stalls long before product-market fit turns into revenue.</p>
    </div>
  </section>

  <section class="ideal">
    <div class="eyebrow">Who We Help</div>
    <h2 class="section-title">IDEAL CLIENT FIT</h2>
    <div class="ideal-cols">
      <div class="ideal-col">
        <h4>SALES LEADERS (CRO / VP)</h4>
        <p>Leaders who need an experienced partner to build process, coach teams and hit ambitious revenue targets.</p>
        <span class="btn btn--outline">Learn More</span>
      </div>
      <div class="ideal-col">
        <h4>FOUNDERS &amp; CEOS</h4>
        <p>Founders ready to step back from selling and hand over a proven, scalable sales engine to their team.</p>
        <span class="btn">Learn More</span>
      </div>
    </div>
  </section>

  <section class="results">
    <div class="eyebrow">Testimonials</div>
    <h2 class="section-title">RESULTS DELIVERED</h2>
    <div class="video-row">
      <div class="video" role="img" aria-label="Client video testimonial"><span class="play"><svg width="7" height="10"><path d="M0 0L7 5L0 10Z" fill="#1d1ddb"/></svg></span></div>
      <div class="video" role="img" aria-label="Client video testimonial"><span class="play"><svg width="7" height="10"><path d="M0 0L7 5L0 10Z" fill="#1d1ddb"/></svg></span></div>
      <div class="video" role="img" aria-label="Client video testimonial"><span class="play"><svg width="7" height="10"><path d="M0 0L7 5L0 10Z" fill="#1d1ddb"/></svg></span></div>
      <div class="video" role="img" aria-label="Client video testimonial"><span class="play"><svg width="7" height="10"><path d="M0 0L7 5L0 10Z" fill="#1d1ddb"/></svg></span></div>
    </div>
  </section>

  <section class="testimonials">
    <div class="quote">
      <div class="quote-mark"><svg width="12" height="10"><path d="M0 10V5Q0 0 5 0V2Q2 2 2 5H5V10ZM7 10V5Q7 0 12 0V2Q9 2 9 5H12V10Z" fill="#fff"/></svg></div>
      <div class="quote-card"><p>Working together transformed how we sell. Within months we had a clear process, a motivated team and a pipeline we could actually forecast. I only wish we had started sooner.</p></div>
      <div class="avatar" role="img" aria-label="Client portrait"></div>
      <div class="quote-name">Daniel Orme</div>
      <div class="quote-role">CEO, SaaS platform</div>
    </div>
    <div class="quote">
      <div class="quote-mark"><svg width="12" height="10"><path d="M0 10V5Q0 0 5 0V2Q2 2 2 5H5V10ZM7 10V5Q7 0 12 0V2Q9 2 9 5H12V10Z" fill="#fff"/></svg></div>
      <div class="quote-card"><p>A practical, hands-on partner who understands early-stage SaaS. The playbooks and coaching gave our reps the confidence to close bigger deals faster than ever before.</p></div>
      <div class="avatar" role="img" aria-label="Client portrait"></div>
      <div class="quote-name">Priya Castell</div>
      <div class="quote-role">Founder, B2B tech firm</div>
    </div>
  </section>

  <section class="recent">
    <div class="eyebrow">Case Studies</div>
    <h2 class="section-title">RECENT SUCCESS</h2>
    <div class="recent-body">
      <div class="recent-tabs">
        <div class="is-active">Scaling a UK analytics startup from $1M to $5M ARR</div>
        <div>Building a US sales team from zero hires</div>
        <div>Entering the US market with a focused GTM plan</div>
      </div>
      <div class="recent-copy">
        <h4>SITUATION</h4>
        <p>The company had reached its first million in revenue through founder sales but lacked structure, reporting and a team able to repeat those wins at scale.</p>
        <p>Deals were slipping, onboarding was inconsistent and the board wanted a credible plan to reach the next stage of growth within eighteen months.</p>
        <h4>ACTION</h4>
        <p>We introduced a clear sales methodology, hired and trained three account executives and built a dashboard that tracked conversion at every stage of the funnel.</p>
        <p>Messaging was refined for two core segments and outbound sequences were tested weekly to find the strongest channels for new pipeline.</p>
        <p>The founders moved from closing every deal to coaching the team on strategic accounts only.</p>
        <h4>RESULT</h4>
        <p>Annual recurring revenue grew fivefold, average deal size rose by forty percent and the company secured new funding on the strength of its sales engine.</p>
        <p>The team continues to run the process independently with quarterly check-ins.</p>
      </div>
    </div>
  </section>

  <section class="plans">
    <div class="eyebrow">How We Work</div>
    <h2 class="section-title">ENGAGEMENT PLANS</h2>
    <div class="plan is-open">
      <div class="plan-head"><span>Growth<small>3 months</small></span><svg width="9" height="6"><path d="M1 5L4.5 1L8 5" stroke="#1d1ddb" stroke-width="1.4" fill="none"/></svg></div>
      <div class="plan-body">
        <div class="plan-group"><h5>GTM STRATEGY</h5>
          <div class="plan-item">Ideal customer profile and market segmentation<span class="tick"><svg width="5" height="4"><path d="M.5 2L2 3.4L4.5 .6" stroke="#fff" fill="none"/></svg></span></div>
          <div class="plan-item">Value proposition and messaging framework<span class="tick"><svg width="5" height="4"><path d="M.5 2L2 3.4L4.5 .6" stroke="#fff" fill="none"/></svg></span></div>
          <div class="plan-item">Pricing and packaging review<span class="tick"><svg width="5" height="4"><path d="M.5 2L2 3.4L4.5 .6" stroke="#fff" fill="none"/></svg></span></div>
        </div>
        <div class="plan-group"><h5>SALES PROCESS</h5>
          <div class="plan-item">Pipeline stages with clear exit criteria<span class="tick"><svg width="5" height="4"><path d="M.5 2L2 3.4L4.5 .6" stroke="#fff" fill="none"/></svg></span></div>
          <div class="plan-item">CRM setup and reporting dashboard<span class="tick"><svg width="5" height="4"><path d="M.5 2L2 3.4L4.5 .6" stroke="#fff" fill="none"/></svg></span></div>
          <div class="plan-item">Outbound playbook and sequences<span class="tick"><svg width="5" height="4"><path d="M.5 2L2 3.4L4.5 .6" stroke="#fff" fill="none"/></svg></span></div>
          <div class="plan-item">Discovery and demo call scripts<span class="tick"><svg width="5" height="4"><path d="M.5 2L2 3.4L4.5 .6" stroke="#fff" fill="none"/></svg></span></div>
        </div>
        <div class="plan-group"><h5>TEAM &amp; COACHING</h5>
          <div class="plan-item">Weekly one-to-one coaching sessions<span class="tick"><svg width="5" height="4"><path d="M.5 2L2 3.4L4.5 .6" stroke="#fff" fill="none"/></svg></span></div>
          <div class="plan-item">Live deal support on key accounts<span class="tick"><svg width="5" height="4"><path d="M.5 2L2 3.4L4.5 .6" stroke="#fff" fill="none"/></svg></span></div>
        </div>
        <div class="plan-group"><h5>REPORTING</h5>
          <div class="plan-item">Monthly board-ready revenue report<span class="tick"><svg width="5" height="4"><path d="M.5 2L2 3.4L4.5 .6" stroke="#fff" fill="none"/></svg></span></div>
          <div class="plan-item">Forecast accuracy review<span class="tick"><svg width="5" height="4"><path d="M.5 2L2 3.4L4.5 .6" stroke="#fff" fill="none"/></svg></span></div>
        </div>
        <div class="plan-group"><h5>HIRING SUPPORT</h5>
          <div class="plan-item">Role scorecards and interview guides<span class="tick"><svg width="5" height="4"><path d="M.5 2L2 3.4L4.5 .6" stroke="#fff" fill="none"/></svg></span></div>
        </div>
      </div>
    </div>
    <div class="plan"><div class="plan-head"><span>Scale<small>6 months</small></span><svg width="9" height="6"><path d="M1 1L4.5 5L8 1" stroke="#16163a" stroke-width="1.4" fill="none"/></svg></div></div>
    <div class="plan"><div class="plan-head"><span>Hypergrowth<small>12 months</small></span><svg width="9" height="6"><path d="M1 1L4.5 5L8 1" stroke="#16163a" stroke-width="1.4" fill="none"/></svg></div></div>
  </section>

  <section class="steps">
    <div class="eyebrow">Our Process</div>
    <h2 class="section-title">SIMPLE STEPS TO GROWTH</h2>
    <p class="steps-intro">A clear, proven path from first conversation to a sales engine that scales with your business.</p>
    <div class="step-grid">
      <div class="step is-first"><div class="step-num">1</div><h4>BOOK A DISCOVERY</h4><p>A free call to understand your goals, market and current sales challenges.</p></div>
      <div class="arrow"><svg width="22" height="10"><path d="M0 5H19M15 1L20 5L15 9" stroke="#1d1ddb" stroke-width="1.4" fill="none"/></svg></div>
      <div class="step"><div class="step-num">2</div><h4>SCHEDULE A MEETING</h4><p>A deep-dive session to review your pipeline, team and go-to-market.</p></div>
      <div class="step"><div class="step-num">3</div><h4>TRANSFORMATION COMMENCES</h4><p>We implement the plan together and coach your team week by week.</p></div>
      <div class="arrow"><svg width="22" height="10"><path d="M22 5H3M7 1L2 5L7 9" stroke="#1d1ddb" stroke-width="1.4" fill="none"/></svg></div>
      <div class="step"><div class="step-num">4</div><h4>SELECT AN ENGAGEMENT</h4><p>Choose the plan that matches your stage and growth ambitions.</p></div>
    </div>
  </section>

  <section class="ready">
    <h2>READY TO START?</h2>
    <p>Book a free discovery call and find out how a fractional sales leader can unlock predictable, repeatable growth for your SaaS business.</p>
    <span class="btn btn--light">Let's Talk</span>
  </section>

  <section class="unlock">
    <div class="unlock-copy">
      <div class="eyebrow">Free Guide</div>
      <h2>UNLOCK 4 STRATEGIES<br>TO BOOST ARR</h2>
      <div class="signup"><span>Enter your email</span><b>Sign Up</b></div>
    </div>
    <div class="unlock-photo" role="img" aria-label="Video of the consultant presenting the guide"><span class="play"><svg width="7" height="10"><path d="M0 0L7 5L0 10Z" fill="#1d1ddb"/></svg></span></div>
  </section>
  <footer class="footer">© Harlow Vance Sales Advisory · All rights reserved</footer>
</main>

<!-- Concept B -->
<main class="page page--b">
  <header class="hero">
    <div class="hero-art" role="img" aria-label="Abstract yellow illustration of a rising growth chart"></div>
    <nav class="nav">
      <div class="brand"><span class="brand-mark"></span><span>Harlow Vance<br>Sales Advisory</span></div>
      <div class="nav-links"><span>Home</span><span>About</span><span>Services</span><span>Results</span><span>Insights</span><span>Contact</span></div>
      <div class="nav-icons"><span></span><span></span><span></span></div>
    </nav>
    <div class="hero-body">
      <h1 class="hero-title">Fractional GTM<br><em>Leadership for SaaS Firms</em></h1>
      <p class="hero-sub">Unlock your SaaS Hyper-growth Potential. Propelling from Launch to $1M ARR, Scaling Seamlessly to $10M ARR.</p>
      <span class="btn">Book a 30-min Discovery Call Today</span>
    </div>
    <div class="logo-row"><span>Vectrona</span><span>Norvale</span><span>Marrowby</span><span>Quillon</span><span>Tallisk</span></div>
  </header>

  <section class="spotlight">
    <div class="eyebrow">Case Study</div>
    <h2 class="section-title">PROJECT SPOTLIGHT</h2>
    <div class="spot-row">
      <div class="spot-img spot-img--city" role="img" aria-label="Looking up at glass office towers"></div>
      <div class="spot-text">
        <h4>SITUATION</h4>
        <p>A seed-funded SaaS platform had strong product interest but no repeatable sales motion, founder-led deals and a stalled pipeline heading into its next round.</p>
        <h4>ACTION</h4>
        <p>We rebuilt the go-to-market plan, defined the ideal customer profile, set up outbound playbooks and coached the first two account executives through live deals.</p>
        <p>Weekly pipeline reviews and clear stage criteria gave the founders confidence in the forecast within one quarter.</p>
      </div>
    </div>
    <div class="spot-row">
      <div class="spot-text">
        <h4>RESULT</h4>
        <p>Qualified pipeline tripled in six months and the team closed its largest enterprise contract to date, setting up a strong Series A story for investors.</p>
        <p>The sales function now runs without founder involvement in every deal, freeing leadership to focus on product and hiring.</p>
      </div>
      <div class="spot-img spot-img--person" role="img" aria-label="Portrait of the consultant at his desk">
        <div class="badge"><b>24</b><small>Years in<br>B2B sales</small></div>
      </div>
    </div>
  </section>

  <section class="stats">
    <div class="stat"><b>$135M<br>OVERALL</b><small>Revenue generated for clients</small></div>
    <div class="stat"><b>$135M<br>OVERALL</b><small>Pipeline created across markets</small></div>
    <div class="stat"><b>$135M<br>OVERALL</b><small>Funding raised by clients</small></div>
  </section>

  <section class="fail">
    <div class="fail-list">
      <div>95% of SaaS firms fail <span>+</span></div>
      <div>We help SaaS to spot where sales fits in <span>+</span></div>
      <div>Leveraging our GTM strategy for SaaS to scale <span>+</span></div>
    </div>
    <div class="fail-copy">
      <h3>95% of SaaS firms fail.</h3>
      <p>Most early-stage SaaS companies never find a repeatable way to sell. Without a clear go-to-market plan, growth stalls long before product-market fit turns into revenue.</p>
    </div>
  </section>

  <section class="ideal">
    <div class="eyebrow">Who We Help</div>
    <h2 class="section-title">IDEAL CLIENT FIT</h2>
    <div class="ideal-cols">
      <div class="ideal-col">
        <h4>SALES LEADERS (CRO / VP)</h4>
        <p>Leaders who need an experienced partner to build process, coach teams and hit ambitious revenue targets.</p>
        <span class="btn btn--outline">Learn More</span>
      </div>
      <div class="ideal-col">
        <h4>FOUNDERS &amp; CEOS</h4>
        <p>Founders ready to step back from selling and hand over a proven, scalable sales engine to their team.</p>
        <span class="btn">Learn More</span>
      </div>
    </div>
  </section>

  <section class="results">
    <div class="eyebrow">Testimonials</div>
    <h2 class="section-title">RESULTS DELIVERED</h2>
    <div class="video-row">
      <div class="video" role="img" aria-label="Client video testimonial"><span class="play"><svg width="7" height="10"><path d="M0 0L7 5L0 10Z" fill="#1d1ddb"/></svg></span></div>
      <div class="video" role="img" aria-label="Client video testimonial"><span class="play"><svg width="7" height="10"><path d="M0 0L7 5L0 10Z" fill="#1d1ddb"/></svg></span></div>
      <div class="video" role="img" aria-label="Client video testimonial"><span class="play"><svg width="7" height="10"><path d="M0 0L7 5L0 10Z" fill="#1d1ddb"/></svg></span></div>
      <div class="video" role="img" aria-label="Client video testimonial"><span class="play"><svg width="7" height="10"><path d="M0 0L7 5L0 10Z" fill="#1d1ddb"/></svg></span></div>
    </div>
  </section>

  <section class="testimonials">
    <div class="quote">
      <div class="quote-mark"><svg width="12" height="10"><path d="M0 10V5Q0 0 5 0V2Q2 2 2 5H5V10ZM7 10V5Q7 0 12 0V2Q9 2 9 5H12V10Z" fill="#fff"/></svg></div>
      <div class="quote-card"><p>Working together transformed how we sell. Within months we had a clear process, a motivated team and a pipeline we could actually forecast. I only wish we had started sooner.</p></div>
      <div class="avatar" role="img" aria-label="Client portrait"></div>
      <div class="quote-name">Daniel Orme</div>
      <div class="quote-role">CEO, SaaS platform</div>
    </div>
    <div class="quote">
      <div class="quote-mark"><svg width="12" height="10"><path d="M0 10V5Q0 0 5 0V2Q2 2 2 5H5V10ZM7 10V5Q7 0 12 0V2Q9 2 9 5H12V10Z" fill="#fff"/></svg></div>
      <div class="quote-card"><p>A practical, hands-on partner who understands early-stage SaaS. The playbooks and coaching gave our reps the confidence to close bigger deals faster than ever before.</p></div>
      <div class="avatar" role="img" aria-label="Client portrait"></div>
      <div class="quote-name">Priya Castell</div>
      <div class="quote-role">Founder, B2B tech firm</div>
    </div>
  </section>

  <section class="recent">
    <div class="eyebrow">Case Studies</div>
    <h2 class="section-title">RECENT SUCCESS</h2>
    <div class="recent-body">
      <div class="recent-tabs">
        <div class="is-active">Scaling a UK analytics startup from $1M to $5M ARR</div>
        <div>Building a US sales team from zero hires</div>
        <div>Entering the US market with a focused GTM plan</div>
      </div>
      <div class="recent-copy">
        <h4>SITUATION</h4>
        <p>The company had reached its first million in revenue through founder sales but lacked structure, reporting and a team able to repeat those wins at scale.</p>
        <p>Deals were slipping, onboarding was inconsistent and the board wanted a credible plan to reach the next stage of growth within eighteen months.</p>
        <h4>ACTION</h4>
        <p>We introduced a clear sales methodology, hired and trained three account executives and built a dashboard that tracked conversion at every stage of the funnel.</p>
        <p>Messaging was refined for two core segments and outbound sequences were tested weekly to find the strongest channels for new pipeline.</p>
        <p>The founders moved from closing every deal to coaching the team on strategic accounts only.</p>
        <h4>RESULT</h4>
        <p>Annual recurring revenue grew fivefold, average deal size rose by forty percent and the company secured new funding on the strength of its sales engine.</p>
        <p>The team continues to run the process independently with quarterly check-ins.</p>
      </div>
    </div>
  </section>

  <section class="plans">
    <div class="eyebrow">How We Work</div>
    <h2 class="section-title">ENGAGEMENT PLANS</h2>
    <div class="plan is-open">
      <div class="plan-head"><span>Growth<small>3 months</small></span><svg width="9" height="6"><path d="M1 5L4.5 1L8 5" stroke="#1d1ddb" stroke-width="1.4" fill="none"/></svg></div>
      <div class="plan-body">
        <div class="plan-group"><h5>GTM STRATEGY</h5>
          <div class="plan-item">Ideal customer profile and market segmentation<span class="tick"><svg width="5" height="4"><path d="M.5 2L2 3.4L4.5 .6" stroke="#fff" fill="none"/></svg></span></div>
          <div class="plan-item">Value proposition and messaging framework<span class="tick"><svg width="5" height="4"><path d="M.5 2L2 3.4L4.5 .6" stroke="#fff" fill="none"/></svg></span></div>
          <div class="plan-item">Pricing and packaging review<span class="tick"><svg width="5" height="4"><path d="M.5 2L2 3.4L4.5 .6" stroke="#fff" fill="none"/></svg></span></div>
        </div>
        <div class="plan-group"><h5>SALES PROCESS</h5>
          <div class="plan-item">Pipeline stages with clear exit criteria<span class="tick"><svg width="5" height="4"><path d="M.5 2L2 3.4L4.5 .6" stroke="#fff" fill="none"/></svg></span></div>
          <div class="plan-item">CRM setup and reporting dashboard<span class="tick"><svg width="5" height="4"><path d="M.5 2L2 3.4L4.5 .6" stroke="#fff" fill="none"/></svg></span></div>
          <div class="plan-item">Outbound playbook and sequences<span class="tick"><svg width="5" height="4"><path d="M.5 2L2 3.4L4.5 .6" stroke="#fff" fill="none"/></svg></span></div>
          <div class="plan-item">Discovery and demo call scripts<span class="tick"><svg width="5" height="4"><path d="M.5 2L2 3.4L4.5 .6" stroke="#fff" fill="none"/></svg></span></div>
        </div>
        <div class="plan-group"><h5>TEAM &amp; COACHING</h5>
          <div class="plan-item">Weekly one-to-one coaching sessions<span class="tick"><svg width="5" height="4"><path d="M.5 2L2 3.4L4.5 .6" stroke="#fff" fill="none"/></svg></span></div>
          <div class="plan-item">Live deal support on key accounts<span class="tick"><svg width="5" height="4"><path d="M.5 2L2 3.4L4.5 .6" stroke="#fff" fill="none"/></svg></span></div>
        </div>
        <div class="plan-group"><h5>REPORTING</h5>
          <div class="plan-item">Monthly board-ready revenue report<span class="tick"><svg width="5" height="4"><path d="M.5 2L2 3.4L4.5 .6" stroke="#fff" fill="none"/></svg></span></div>
          <div class="plan-item">Forecast accuracy review<span class="tick"><svg width="5" height="4"><path d="M.5 2L2 3.4L4.5 .6" stroke="#fff" fill="none"/></svg></span></div>
        </div>
        <div class="plan-group"><h5>HIRING SUPPORT</h5>
          <div class="plan-item">Role scorecards and interview guides<span class="tick"><svg width="5" height="4"><path d="M.5 2L2 3.4L4.5 .6" stroke="#fff" fill="none"/></svg></span></div>
        </div>
      </div>
    </div>
    <div class="plan"><div class="plan-head"><span>Scale<small>6 months</small></span><svg width="9" height="6"><path d="M1 1L4.5 5L8 1" stroke="#16163a" stroke-width="1.4" fill="none"/></svg></div></div>
    <div class="plan"><div class="plan-head"><span>Hypergrowth<small>12 months</small></span><svg width="9" height="6"><path d="M1 1L4.5 5L8 1" stroke="#16163a" stroke-width="1.4" fill="none"/></svg></div></div>
  </section>

  <section class="steps">
    <div class="eyebrow">Our Process</div>
    <h2 class="section-title">SIMPLE STEPS TO GROWTH</h2>
    <p class="steps-intro">A clear, proven path from first conversation to a sales engine that scales with your business.</p>
    <div class="step-grid">
      <div class="step is-first"><div class="step-num">1</div><h4>BOOK A DISCOVERY</h4><p>A free call to understand your goals, market and current sales challenges.</p></div>
      <div class="arrow"><svg width="22" height="10"><path d="M0 5H19M15 1L20 5L15 9" stroke="#1d1ddb" stroke-width="1.4" fill="none"/></svg></div>
      <div class="step"><div class="step-num">2</div><h4>SCHEDULE A MEETING</h4><p>A deep-dive session to review your pipeline, team and go-to-market.</p></div>
      <div class="step"><div class="step-num">3</div><h4>TRANSFORMATION COMMENCES</h4><p>We implement the plan together and coach your team week by week.</p></div>
      <div class="arrow"><svg width="22" height="10"><path d="M22 5H3M7 1L2 5L7 9" stroke="#1d1ddb" stroke-width="1.4" fill="none"/></svg></div>
      <div class="step"><div class="step-num">4</div><h4>SELECT AN ENGAGEMENT</h4><p>Choose the plan that matches your stage and growth ambitions.</p></div>
    </div>
  </section>

  <section class="ready">
    <h2>READY TO START?</h2>
    <p>Book a free discovery call and find out how a fractional sales leader can unlock predictable, repeatable growth for your SaaS business.</p>
    <span class="btn btn--light">Let's Talk</span>
  </section>

  <section class="unlock">
    <div class="unlock-copy">
      <div class="eyebrow">Free Guide</div>
      <h2>UNLOCK 4 STRATEGIES<br>TO BOOST ARR</h2>
      <div class="signup"><span>Enter your email</span><b>Sign Up</b></div>
    </div>
    <div class="unlock-photo" role="img" aria-label="Video of the consultant presenting the guide"><span class="play"><svg width="7" height="10"><path d="M0 0L7 5L0 10Z" fill="#1d1ddb"/></svg></span></div>
  </section>
  <footer class="footer">© Harlow Vance Sales Advisory · All rights reserved</footer>
</main>

</body>
</html>
```